Heritage Hollow Business Cards

Require a business card design. <br/><br/>Needs to include logo (either round or long version) plus these details:<br/>Maya Torvel<br/>Heritage Hollow<br/>maya@quonbrook.com.au<br/>02 6481 7390<br/>PO Box Glenwarra NSW 2913<br/>www.heritagehollow.com.au<br/><br/>I need in an editable format so that I can create for multiple staff members. <br/><br/>

Target Market(s)

We are an online store selling renovation products to home owners are builders. Looking for a classic classy design.

Industry/Entity Type

Home And Garden

Contact Information for Business Card

Maya Torvel
Heritage Hollow
maya@quonbrook.com.au
02 6481 7390
PO Box Glenwarra NSW 2913
www.heritagehollow.com.au

Colors

Designer to choose colors to be used in the design.

Requirements
Must have
• Must include Logo.

```html
<!DOCTYPE html>
<html lang="en">
<head>
<meta charset="utf-8">
<title>Heritage Hollow Business Cards</title>
<link rel="stylesheet" href="https://fonts.googleapis.com/css2?family=Roboto:wght@400;700&display=swap">
<style>
  :root {
    --canvas-bg: #2a2a2a;
    --card-dark: #1c1c1c;
    --card-light: #ffffff;
    --ink: #1a1a1a;
    --ink-soft: #3a3a3a;
    --rule: #555555;
    --silver: #bdbdbd;
  }
  * { margin: 0; padding: 0; box-sizing: border-box; }
  html, body { width: 1200px; height: 895px; overflow: hidden; }
  body {
    background: var(--canvas-bg);
    font-family: "Roboto", Arial, sans-serif;
    position: relative;
  }
  .card {
    position: absolute;
    top: 282px;
    width: 540px;
    height: 330px;
    box-shadow: 0 10px 30px rgba(0,0,0,0.5);
  }
  .card-back { left: 40px; background: var(--card-dark); }
  .card-front { left: 620px; background: var(--card-light); color: var(--ink); }

  /* back */
  .back-mark {
    position: absolute;
    left: 50%; top: 50%;
    transform: translate(-50%, -50%);
    display: flex; align-items: center; gap: 14px;
  }
  .back-mark .mark-circle {
    width: 40px; height: 40px; border: 2px solid var(--silver); border-radius: 50%;
  }
  .back-mark .mark-name {
    color: var(--silver); font-size: 30px; font-weight: 400;
  }

  /* front */
  .brand {
    position: absolute; left: 34px; top: 108px;
    display: flex; align-items: center; gap: 14px;
  }
  .brand .mark-circle {
    width: 44px; height: 44px; border: 2px solid var(--ink); border-radius: 50%;
  }
  .brand .mark-name { font-size: 34px; font-weight: 400; color: var(--ink); }

  .person {
    position: absolute; right: 26px; top: 40px; text-align: right;
  }
  .person-name {
    font-size: 21px; font-weight: 700; letter-spacing: 0.5px;
    padding-bottom: 4px;
  }
  .person-rule {
    position: absolute; right: 26px; top: 70px; width: 300px;
    border-top: 1px solid var(--rule);
  }
  .person-details {
    position: absolute; right: 26px; top: 78px; text-align: right;
    font-size: 14px; line-height: 1.35; color: var(--ink-soft);
  }

  .contact-rule {
    position: absolute; left: 34px; bottom: 98px; width: 300px;
    border-top: 1px solid var(--rule);
  }
  .contact-list {
    position: absolute; left: 34px; bottom: 18px; list-style: none;
    font-size: 15px; line-height: 1.6; color: var(--ink);
  }
  .contact-list li { display: flex; align-items: center; gap: 12px; }
  .contact-list svg { width: 13px; height: 13px; fill: var(--ink); flex: none; }
</style>
</head>
<body>
  <section class="card card-back" aria-label="Card back">
    <div class="back-mark">
      <span class="mark-circle"></span>
      <span class="mark-name">Heritage Hollow</span>
    </div>
  </section>

  <section class="card card-front" aria-label="Card front">
    <div class="brand">
      <span class="mark-circle"></span>
      <span class="mark-name">Heritage Hollow</span>
    </div>

    <div class="person"><div class="person-name">MAYA TORVEL</div></div>
    <div class="person-rule"></div>
    <div class="person-details">
      Heritage Hollow<br>
      PO Box Glenwarra<br>
      NSW 2913
    </div>

    <div class="contact-rule"></div>
    <ul class="contact-list">
      <li>
        <svg viewBox="0 0 16 16" aria-hidden="true"><path d="M1 5c0-2 2-3 7-3s7 1 7 3v1h-3V5H4v1H1zM3 7h10l1 7H2zM8 9a2 2 0 1 0 0 4a2 2 0 1 0 0-4z"/></svg>
        02 6481 7390
      </li>
      <li>
        <svg viewBox="0 0 16 16" aria-hidden="true"><path d="M1 3h14v10H1zM2.5 4.5v7h11v-7L8 9z" fill-rule="evenodd"/></svg>
        maya@quonbrook.com.au
      </li>
      <li>
        <svg viewBox="0 0 16 16" aria-hidden="true"><circle cx="8" cy="8" r="7"/><path d="M1 8h14M8 1c-3 3-3 11 0 14M8 1c3 3 3 11 0 14" stroke="#fff" stroke-width="1" fill="none"/></svg>
        www.heritagehollow.com.au
      </li>
    </ul>
  </section>
</body>
</html>
```